Mobile Game identical to "Letter Orbit"

We need a design for mobile game identical to "Letter Orbit" you can get from app store using this link https://quickstorelink.example/us/tzvnR.k
playstore link: https://apps.samplemarket.example/store/apps/details?id=se.fenwoodgames.letterorbit&hl=en

- App name will be : Tangle
- For iOS and Android
- Same Letter Orbit features exactly but in different design.
- Ads banner will be overall app screens
- Some kind of animation is needed in the game , designer has to provide.

Requirements
Must have
• - Same Letter Orbit Features and steps
• - Some Animation
• - Game will be in arabic i will help to provide needed text

```html
<!DOCTYPE html>
<html lang="en">
<head>
<meta charset="utf-8">
<title>Tangle – Level Screen</title>
<link href="https://fonts.googleapis.com/css2?family=Cabin+Sketch:wght@400;700&family=Patrick+Hand&family=Rokkitt:wght@700&family=Roboto:wght@500&display=swap" rel="stylesheet">
<style>
  :root {
    --status-bg: #0c0c0c;
    --status-text: #ffffff;
    --shelf-top: #f4e2c4;
    --shelf-bottom: #e8cfa4;
    --shelf-edge: #b98b52;
    --title-ink: #c0702a;
    --wood-light: #f2dfbd;
    --wood-mid: #e7cc9e;
    --wood-grain: rgba(170,120,60,0.14);
    --frame-outer: #c8721f;
    --frame-inner: #e49133;
    --tile-bg: #5b5b5b;
    --tile-empty: #2f2f2f;
    --board-bg: #262626;
    --tile-text: #f2f2f2;
    --chalk-green: #3f7d2c;
    --chalk-green-dark: #336a23;
    --chalk-edge: #9a6b34;
    --chalk-white: #f3f5ea;
    --ad-bg1: #f3b13e;
    --ad-bg2: #8fc6e8;
  }
  * { box-sizing: border-box; margin: 0; padding: 0; }
  html, body { width: 683px; height: 1200px; overflow: hidden; background: #ffffff; }
  .screen { position: relative; width: 683px; height: 1200px; overflow: hidden; }

  .status-bar {
    height: 38px; background: var(--status-bg); color: var(--status-text);
    font-family: "Roboto", sans-serif; font-size: 20px;
    display: flex; align-items: center; justify-content: space-between; padding: 0 14px;
  }
  .status-left { display: flex; align-items: center; gap: 8px; }
  .signal { display: flex; gap: 3px; align-items: flex-end; }
  .signal span { display: block; width: 4px; background: #fff; }
  .status-right { display: flex; align-items: center; gap: 10px; }
  .battery { width: 40px; height: 17px; border: 2px solid #fff; border-radius: 3px; padding: 2px; position: relative; }
  .battery::after { content: ""; position: absolute; right: -5px; top: 4px; width: 3px; height: 6px; background: #fff; }
  .battery i { display: block; height: 100%; width: 80%; background: #fff; }

  .shelf {
    position: absolute; top: 38px; left: 0; width: 683px; height: 140px;
    background: linear-gradient(var(--shelf-top), var(--shelf-bottom));
    border-bottom: 6px solid var(--shelf-edge);
    display: flex; align-items: center; justify-content: center; gap: 18px;
  }
  .app-mark { width: 26px; height: 26px; background: var(--title-ink); border-radius: 4px; }
  .app-title {
    font-family: "Rokkitt", serif; font-weight: 700; font-size: 64px;
    letter-spacing: 10px; color: var(--title-ink); line-height: 1;
  }

  .wood-wall {
    position: absolute; top: 184px; left: 0; width: 683px; height: 556px;
    background:
      repeating-linear-gradient(90deg, transparent 0 26px, var(--wood-grain) 26px 28px, transparent 28px 61px),
      linear-gradient(var(--wood-light), var(--wood-mid));
  }
  .hanger { position: absolute; top: 40px; left: 241px; }

  .letter-board {
    position: absolute; top: 94px; left: 125px; width: 432px; height: 428px;
    background: linear-gradient(var(--frame-inner), var(--frame-outer));
    border-radius: 10px; padding: 18px;
    box-shadow: 0 6px 10px rgba(0,0,0,0.25);
  }
  .letter-grid {
    width: 100%; height: 100%; background: var(--board-bg);
    display: grid; grid-template-columns: repeat(5, 1fr); grid-template-rows: repeat(5, 1fr);
    gap: 5px; padding: 5px;
  }
  .tile {
    background: var(--tile-bg); color: var(--tile-text);
    font-family: "Rokkitt", serif; font-weight: 700; font-size: 40px;
    display: flex; align-items: center; justify-content: center;
  }
  .tile.empty { background: var(--tile-empty); }

  .chalkboard {
    position: absolute; top: 740px; left: 0; width: 683px; height: 358px;
    background: radial-gradient(ellipse at 50% 40%, var(--chalk-green), var(--chalk-green-dark));
    border-top: 8px solid var(--chalk-edge);
    color: var(--chalk-white);
  }
  .chalk-heading { position: absolute; top: 42px; width: 100%; text-align: center; font-family: "Patrick Hand", cursive; font-size: 34px; }
  .word-slot { position: absolute; font-family: "Cabin Sketch", cursive; font-weight: 700; font-size: 46px; letter-spacing: 10px; }
  .word-found { top: 100px; left: 64px; }
  .word-found span { display: inline-block; border-bottom: 4px solid var(--chalk-white); line-height: 1; margin-right: 2px; }
  .blanks { display: flex; gap: 12px; }
  .blanks i { display: block; width: 34px; height: 4px; background: var(--chalk-white); }
  .blank-row-1 { top: 150px; left: 350px; }
  .blank-row-2 { top: 212px; left: 300px; }

  .controls { position: absolute; top: 264px; left: 0; width: 100%; display: flex; justify-content: center; gap: 22px; }
  .chalk-btn {
    height: 56px; border: 3px solid var(--chalk-white); border-radius: 14px;
    font-family: "Patrick Hand", cursive; font-size: 26px; color: var(--chalk-white);
    display: flex; align-items: center; justify-content: center; padding: 0 18px;
  }
  .btn-levels { width: 196px; }
  .btn-refresh { width: 104px; }
  .btn-hint { width: 196px; }

  .ad-banner {
    position: absolute; top: 1098px; left: 0; width: 683px; height: 102px;
    background: linear-gradient(90deg, var(--ad-bg1), #e77e4a 45%, var(--ad-bg2));
  }
</style>
</head>
<body>
<div class="screen">
  <header class="status-bar">
    <div class="status-left">
      <div class="signal"><span style="height:6px"></span><span style="height:9px"></span><span style="height:12px"></span><span style="height:15px"></span><span style="height:18px"></span></div>
      <span>NX</span>
      <svg width="22" height="16" viewBox="0 0 22 16"><path d="M11 15 L2 6 A13 13 0 0 1 20 6 Z" fill="#fff"/></svg>
    </div>
    <span>1:57 PM</span>
    <div class="status-right">
      <svg width="18" height="18" viewBox="0 0 18 18"><circle cx="9" cy="9" r="7" fill="none" stroke="#fff" stroke-width="2"/><path d="M9 5v4l3 2" stroke="#fff" stroke-width="2" fill="none"/></svg>
      <div class="battery"><i></i></div>
    </div>
  </header>

  <section class="shelf">
    <span class="app-mark" aria-hidden="true"></span>
    <h1 class="app-title">TANGLE</h1>
  </section>

  <section class="wood-wall">
    <svg class="hanger" width="200" height="60" viewBox="0 0 200 60">
      <path d="M20 58 L100 14 L180 58" stroke="#7a4a1e" stroke-width="3" fill="none"/>
      <circle cx="100" cy="12" r="9" fill="#9a6a36"/>
      <circle cx="100" cy="12" r="4" fill="#5e3a16"/>
    </svg>
    <div class="letter-board">
      <div class="letter-grid">
        <div class="tile">A</div><div class="tile">X</div><div class="tile">I</div><div class="tile">C</div><div class="tile empty"></div>
        <div class="tile">V</div><div class="tile empty"></div><div class="tile">S</div><div class="tile">J</div><div class="tile">N</div>
        <div class="tile empty"></div><div class="tile">R</div><div class="tile">D</div><div class="tile">P</div><div class="tile empty"></div>
        <div class="tile">E</div><div class="tile">T</div><div class="tile">A</div><div class="tile">U</div><div class="tile">H</div>
        <div class="tile">Y</div><div class="tile">U</div><div class="tile">O</div><div class="tile empty"></div><div class="tile">E</div>
      </div>
    </div>
  </section>

  <section class="chalkboard">
    <p class="chalk-heading">words to find</p>
    <div class="word-slot word-found"><span>C</span><span>L</span><span>O</span><span>U</span><span>D</span></div>
    <div class="word-slot blanks blank-row-1"><i></i><i></i><i></i><i></i><i></i></div>
    <div class="word-slot blanks blank-row-2"><i></i><i></i><i></i><i></i><i></i><i></i></div>
    <nav class="controls">
      <div class="chalk-btn btn-levels">&lt;&lt;LEVELS</div>
      <div class="chalk-btn btn-refresh">
        <svg width="34" height="34" viewBox="0 0 34 34" fill="none" stroke="#f3f5ea" stroke-width="3.5">
          <path d="M27 13 A11 11 0 0 0 7 12"/><path d="M7 21 A11 11 0 0 0 27 22"/>
          <path d="M27 5 V13 H19"/><path d="M7 29 V21 H15"/>
        </svg>
      </div>
      <div class="chalk-btn btn-hint">HINT!(250)</div>
    </nav>
  </section>

  <div class="ad-banner" role="img" aria-label="Advertisement banner with game artwork"></div>
</div>
</body>
</html>
```